Need to have a client log in screen for work orders and estimate requests.
Nice informational landing page.

Stonefield is a full service general contractor servicing apartment complexes;
maintenance of grounds and apartments - remodeling and construction.

Design Specifics: We are pretty open here. Some good examples are
www.oakhavenworks.com , pellarestates.com and www.norvo7building.com

For the site we need:
Homepage - to explain services
Roofing page
Apartment Page
Client Portal - where clients can set up accounts to set up work/estimate request that will be routed to our email

--Will need coding, plan to host site on Wordpress

Target Market(s)

Multi family, Residential and commercial clients

Industry/Entity Type

Construction

Coding

Coded - Design and coding required

Number of Pages Required

3 page

Font styles to use
Serif

Requirements
Must have
• Client portal
Nice to have
• Not sure. please advise

```html
<!DOCTYPE html>
<html lang="en">
<head>
<meta charset="utf-8">
<title>Stonefield Construction</title>
<link rel="stylesheet" href="https://fonts.googleapis.com/css2?family=Roboto:wght@400;500;700&family=Roboto+Condensed:wght@400;700&family=Open+Sans:wght@400&display=swap">
<style>
  :root {
    --brand-red: #b30f10;
    --ink: #222222;
    --body-text: #474747;
    --nav-text: #1e1e1e;
    --hero-panel: rgba(18, 28, 44, 0.86);
    --accent-yellow: #ffee00;
    --accent-orange: #ffb000;
    --left-bg: #f7f3fb;
    --right-bg: #efe9f6;
    --link-blue: #2a4fc4;
    --white: #ffffff;
  }
  * { box-sizing: border-box; margin: 0; padding: 0; }
  html, body { width: 1070px; height: 1200px; overflow: hidden; background: var(--white); }
  body { position: relative; font-family: "Roboto", Arial, sans-serif; }

  .contact-bar {
    position: absolute; left: 0; top: 0; width: 1070px; height: 36px;
    background: var(--brand-red); color: var(--white);
    font-size: 12px; letter-spacing: 0.3px;
    display: flex; align-items: center; justify-content: center;
  }
  .contact-bar em { font-weight: 700; }

  .site-header { position: absolute; left: 0; top: 36px; width: 1070px; height: 133px; background: var(--white); }
  .brand {
    position: absolute; left: 84px; top: 48px;
    display: flex; align-items: center; gap: 10px;
    font-family: "Roboto", Arial, sans-serif; font-weight: 700; font-size: 22px;
    color: var(--ink); letter-spacing: 0.5px;
  }
  .brand-mark { width: 22px; height: 22px; background: var(--brand-red); }
  .main-nav { position: absolute; top: 66px; left: 448px; display: flex; gap: 0; }
  .main-nav a {
    font-size: 13px; color: var(--nav-text); text-decoration: none; margin-right: 28px;
  }
  .main-nav a.is-active { color: var(--brand-red); }

  .hero { position: absolute; left: 0; top: 169px; width: 1070px; height: 573px; }
  .hero-photo {
    position: absolute; inset: 0;
    background: linear-gradient(100deg, #5a8fd0 0%, #2f5288 18%, #c89a5c 30%, #e8c890 42%, #2b3e5e 55%, #1a2a44 80%, #2a4a66 100%);
  }
  .hero-panel {
    position: absolute; left: 535px; top: 0; width: 535px; height: 573px;
    background: var(--hero-panel);
  }
  .hero-title {
    position: absolute; left: 560px; top: 66px;
    font-family: "Roboto Condensed", Arial, sans-serif; font-weight: 700;
    font-size: 58px; line-height: 70px; color: var(--white);
  }
  .hero-subtitle {
    position: absolute; left: 560px; top: 222px; width: 430px;
    font-family: "Roboto Condensed", Arial, sans-serif; font-size: 23px; line-height: 29px;
    color: var(--accent-yellow);
  }
  .hero-text {
    position: absolute; left: 560px; top: 313px; width: 430px;
    font-family: "Open Sans", Arial, sans-serif; font-size: 14px; line-height: 17px; color: var(--white);
  }

  .info-left { position: absolute; left: 0; top: 742px; width: 529px; height: 448px; background: var(--left-bg); }
  .info-right { position: absolute; left: 529px; top: 742px; width: 541px; height: 448px; background: var(--right-bg); }
  .section-title {
    position: absolute; top: 18px;
    font-family: "Roboto", Arial, sans-serif; font-weight: 700; font-size: 29px; color: var(--ink);
  }
  .title-rule {
    position: absolute; top: 68px; height: 4px;
    background: linear-gradient(90deg, var(--ink) 0 80px, var(--accent-orange) 80px);
  }
  .info-left .section-title { left: 70px; }
  .info-left .title-rule { left: 70px; width: 397px; }
  .info-right .section-title { left: 6px; }
  .info-right .title-rule { left: 6px; width: 443px; }

  .intro-copy {
    position: absolute; left: 70px; top: 92px; width: 396px;
    font-family: "Roboto Condensed", Arial, sans-serif; font-size: 12.5px; line-height: 19px; color: var(--body-text);
  }
  .intro-copy p + p { margin-top: 19px; }

  .guarantee-copy {
    position: absolute; left: 17px; top: 90px; width: 190px;
    font-family: "Roboto Condensed", Arial, sans-serif; font-size: 14.5px; line-height: 25.5px; color: var(--body-text);
  }
  .director-photo {
    position: absolute; left: 259px; top: 84px; width: 172px; height: 252px;
    background: linear-gradient(180deg, #e9e4ee 0%, #4a4d55 30%, #59697e 55%, #8e3b32 78%, #b9a33a 100%);
    border-radius: 4px;
  }
  .signature {
    position: absolute; left: 60px; top: 366px; width: 86px; height: 34px;
    background: linear-gradient(90deg, rgba(32,40,120,0.15), rgba(32,40,120,0.35), rgba(32,40,120,0.15));
    border-radius: 3px;
  }
  .director-credit {
    position: absolute; left: 243px; top: 369px; width: 205px; text-align: center;
    font-size: 13px; line-height: 19px; color: var(--ink);
  }
  .director-credit .director-name { color: var(--link-blue); }
  .director-credit .company-line { color: var(--brand-red); font-weight: 700; display: block; }
</style>
</head>
<body>
  <div class="contact-bar">For any queries please call us at&nbsp;<em>01632 4470 2185</em>&nbsp;or mail us at&nbsp;<em>info@stonefieldconstruction.com</em></div>

  <header class="site-header">
    <div class="brand"><span class="brand-mark"></span>STONEFIELD CONSTRUCTION</div>
    <nav class="main-nav">
      <a href="#" class="is-active">HOME</a>
      <a href="#">ABOUT</a>
      <a href="#">ROOFING</a>
      <a href="#">ROOFING</a>
      <a href="#">CLIENT</a>
      <a href="#">PROJECTS</a>
      <a href="#">CONTACT US</a>
    </nav>
  </header>

  <section class="hero">
    <div class="hero-photo" role="img" aria-label="Modern two-storey house with lit glass walls at dusk beside a pool"></div>
    <div class="hero-panel"></div>
    <h1 class="hero-title">LOREM IPSUM<br>DOLOR SIT AMET</h1>
    <p class="hero-subtitle">LOREL IPSUM DOLOT AMET EST DI MARIA NUNO VALENCIA</p>
    <p class="hero-text">Ut pharetra aue nec augentumonec in velit vel ipsum auliypam elit magna Donec porta diam eu massa. Quisue diam lorem intdum vitaapibus ac scelerisque taeede. Donec eget tellus non erat lin fermentum.</p>
  </section>

  <section class="info-left">
    <h2 class="section-title">WHO WE ARE</h2>
    <div class="title-rule"></div>
    <div class="intro-copy">
      <p>Nunc commodo metus velit, ac luctus ante vehicula sit amet. Nunc lobortis sodales justo sit amet semper. Fusce luctus ligula nisi, vel blandit est porta ac. Nullam sodales rutrum iaculis. In a vestibulum lacus. Integer nunc odio, dignissim fringilla gravida eu, egestas in nisi. Pellentesque tellus diam, eleifend et accumsan non, vulputate eu urna. Sed facilisis odio quis libero mollis, sed pretium velit pretium. Sed vitae tempor felis, sit amet maximus massa.</p>
      <p>Pellentesque habitant morbi tristique senectus et netus et malesuada fames ac turpis egestas. Aenean eu condimentum elit. Praesent et ipsum sed lectus dictum efficitur. Pellentesque vel aliquam leo, eu varius quam. Vivamus ac justo metus. Sed eu tellus sit amet risus gravida pulvinar et id lorem.</p>
    </div>
  </section>

  <section class="info-right">
    <h2 class="section-title">STONEFIELD GUARANTEE</h2>
    <div class="title-rule"></div>
    <p class="guarantee-copy">Stonefield promises to be the most trusted Building Construction Company you can engage in England. I personally guarantee unparalleled value for money, with an exacting attention to every detail to ensure your building project exceeds your expectations.</p>
    <div class="director-photo" role="img" aria-label="Project director standing arms crossed behind a curved brick wall with yellow flowers"></div>
    <div class="signature" role="img" aria-label="Handwritten signature of the project director"></div>
    <p class="director-credit"><span class="director-name">Martin Hale</span>, Senior Project Director<span class="company-line">STONEFIELD CONSTRUCTION</span></p>
  </section>
</body>
</html>
```